Poster for the 'LFA Monthly Draw'

We are a parents association for a senior school and have a number of money raising activities.

We require a poster a lucky draw where parents who subscribe £20 for the school year are entered into a monthly cash prize draw.

Draws are performed monthly. Some detail about it is available here

http://www.larchfield.example-school.uk/lfa/what-is-350-circle

We are changing the name from 'The 350 circle' to 'LFA Monthly draw', although we don't need the name change highlighted or noted on the poster

A logo is available on the word document application at the above link. Not sure of the quality. I can look to obtain a better resolution, but no promises.

A brief overview of the LFA can be read here for any thoughts / inspiration.

We don't want any reference to specific items purchased, unless we can easily update this on the poster ourselves.

http://www.larchfield.example-school.uk/lfa

Target Market(s)

Parents of school kids aged 13 to 17 from whom we are trying to raise contributions to so as to provide funding to school departments who have need to additional items that are not available via the school budget.

Industry/Entity Type

School

Requirements
Must have
• LFA Parents association logo, as in the current 350 circle application, should appear.
• Reference to the amount to be contributed of £20 for the year.
• Reference to the monthly prize draw amounts of
• 1st prize - £30
• 2nd prize - £20
• 3rd Prize £10
• Please note all spellings are to be UK english, not American english.
• Payment methods should be highlighted being
• - Trenvolo- via the school website
• - Cash
• - Cheque - Payable to Larchfield’s Parents’ Association 350 Circle
• No specific colour scheme, although you will see from the school website what the colours are and this should have some representation, but not overbearing.
• The following text is to appear
• The LFA Monthly Draw is a fundraiser for the Larchfield Parent Association. We raise funds to provide the best possible resources and facilities, for your children, to enhance their learning.
• Thank you for your support of the LFA
Nice to have
• The font type is not to critical, however, it should be easy to read in a short space of time as people are walking past, so not excessive amounts of text detail and not to small a font.

```html
<!DOCTYPE html>
<html lang="en-GB">
<head>
<meta charset="utf-8">
<title>LFA Monthly Draw</title>
<link href="https://fonts.googleapis.com/css2?family=Anton&family=Open+Sans:wght@400;600;700&family=Kalam:wght@700&display=swap" rel="stylesheet">
<style>
  :root {
    --maroon: #8b1a3e;
    --ink: #111111;
    --paper: #ffffff;
    --photo-light: #d9d6d2;
    --photo-dark: #8e8a86;
  }
  html, body { margin: 0; padding: 0; overflow: hidden; background: var(--paper); }
  .poster {
    position: relative;
    width: 855px;
    height: 1200px;
    overflow: hidden;
    background: var(--paper);
    font-family: "Open Sans", Arial, sans-serif;
  }
  .masthead {
    position: absolute; left: 0; top: 0; width: 855px; height: 178px;
    background: var(--maroon);
  }
  .masthead svg { position: absolute; left: 0; top: 0; }
  .masthead__title { font-family: "Anton", Impact, sans-serif; fill: var(--paper); }
  .masthead__strap { font-family: "Open Sans", Arial, sans-serif; font-weight: 700; fill: var(--paper); }
  .hero-photo {
    position: absolute; left: 0; top: 178px; width: 855px; height: 452px;
    background: linear-gradient(100deg, var(--photo-light) 0%, #cfcac5 55%, var(--photo-dark) 100%);
  }
  .headline-stack { position: absolute; left: 0; top: 630px; }
  .headline { font-family: "Anton", Impact, sans-serif; }
  .headline--maroon { fill: var(--maroon); }
  .headline--ink { fill: var(--ink); }
  .headline__note { font-family: "Open Sans", Arial, sans-serif; font-weight: 700; fill: var(--maroon); }
  .about {
    position: absolute; left: 36px; top: 976px; width: 330px; margin: 0;
    font-size: 17px; line-height: 23.5px; color: var(--ink);
  }
  .school-name {
    position: absolute; left: 382px; top: 978px; width: 430px; height: 74px;
  }
  .school-name__mark {
    position: absolute; left: 4px; top: 0; width: 72px; height: 72px;
    border-radius: 50%; background: var(--maroon);
  }
  .school-name__text {
    position: absolute; left: 90px; top: 0; margin: 0;
    font-family: "Open Sans", Arial, sans-serif; font-weight: 400;
    font-size: 40px; line-height: 50px; color: var(--maroon); white-space: nowrap;
  }
  .school-name__tagline {
    position: absolute; right: 10px; top: 52px; margin: 0;
    font-size: 12px; line-height: 16px; color: var(--maroon);
  }
  .thanks {
    position: absolute; left: 326px; top: 1056px; margin: 0;
    font-family: "Kalam", "Comic Sans MS", cursive; font-weight: 700;
    font-size: 27px; line-height: 34px; color: var(--ink); white-space: nowrap;
  }
  .more-info {
    position: absolute; right: 40px; top: 1104px; margin: 0;
    font-weight: 700; font-size: 17px; line-height: 24px; color: var(--maroon); white-space: nowrap;
  }
  .payment-bar {
    position: absolute; left: 0; top: 1136px; width: 855px; height: 64px;
    background: var(--maroon); color: var(--paper);
    display: flex; align-items: center; justify-content: center;
    font-size: 15.5px; margin: 0;
  }
  .payment-bar strong { font-weight: 700; }
</style>
</head>
<body>
<div class="poster">

  <header class="masthead">
    <svg width="855" height="178" viewBox="0 0 855 178">
      <text class="masthead__title" x="427.5" y="115" text-anchor="middle" font-size="86" textLength="740" lengthAdjust="spacingAndGlyphs">ATTENTION PARENTS!</text>
      <text class="masthead__strap" x="427.5" y="150" text-anchor="middle" font-size="17" textLength="740" lengthAdjust="spacingAndGlyphs">RAISING FUNDS FOR OUR SCHOOL ISN'T ROCKET SCIENCE ... IT'S PEOPLE CHEMISTRY!</text>
    </svg>
  </header>

  <div class="hero-photo" role="img" aria-label="Photograph of a scientist holding a blackboard reading: Monthly Prize Draw, 1st prize £30, 2nd prize £20, 3rd prize £10"></div>

  <svg class="headline-stack" width="855" height="345" viewBox="0 0 855 345">
    <text class="headline headline--maroon" x="427.5" y="64" text-anchor="middle" font-size="48" textLength="690" lengthAdjust="spacingAndGlyphs">DISCOVER THE FORMULA FOR SUCCESSFUL</text>
    <text class="headline headline--maroon" x="427.5" y="181" text-anchor="middle" font-size="114" textLength="690" lengthAdjust="spacingAndGlyphs">FUNDRAISING</text>
    <text class="headline headline--ink" x="427.5" y="225" text-anchor="middle" font-size="31" textLength="690" lengthAdjust="spacingAndGlyphs">CONTRIBUTE JUST £20 FOR THE YEAR FOR A ONE OFF CHANCE TO</text>
    <text class="headline headline--ink" x="427.5" y="308" text-anchor="middle" font-size="80" textLength="700" lengthAdjust="spacingAndGlyphs">WIN UP TO £30 A MONTH!</text>
    <text class="headline__note" x="427.5" y="334" text-anchor="middle" font-size="17" textLength="790" lengthAdjust="spacingAndGlyphs">(Yes, that's less than 50 pence a week for a chance to win £30, £20 or £10 each month!)</text>
  </svg>

  <p class="about">The LFA Monthly Draw is a fundraiser<br>for the Larchfield Parent Association.<br>We raise funds to provide the best<br>possible resources and facilities,<br>for your children, to enhance<br>their learning.</p>

  <div class="school-name">
    <span class="school-name__mark"></span>
    <p class="school-name__text">Larchfield School</p>
    <p class="school-name__tagline">A Specialist Sports and Science College</p>
  </div>

  <p class="thanks">Thank you for your support of the LFA</p>
  <p class="more-info">Discover more at: www.larchfield.example-school.uk/lfa</p>

  <p class="payment-bar">Payment methods&nbsp;•&nbsp;<strong>Trenvolo</strong>&nbsp;- via the school website&nbsp;•&nbsp;<strong>Cash</strong>&nbsp;•&nbsp;<strong>Cheque</strong>&nbsp;- Payable to Larchfield’s Parents’ Association</p>

</div>
</body>
</html>
```